Property Management Services - Capabilities Overview

We need a letter-sized brochure, preferably with a cover page, 2 pages of content, and back page. We are a multi-family property management firm, Indianapolis HQ, and we need this overview as an initial piece of collateral for investors who own Multifamily properties and are a looking for professional management services. We would like to include more photos, visuals, graphs, etc. than long-winded paragraphs. Our colors are orange, dark blue, and dark gray. We are fine with stock photos of apartment communities for some of the content. Will also upload sample brochures from competitors as well as current portfolio photos in the upload section. Feel free to use as much or as little as appropriate.

Target Market(s)

Real Estate Investors, Real Estate Brokers, Multifamily Investment Advisors

Industry/Entity Type

Property Management

Colors
0655a3
333333
f78f20

Requirements
Must have
• Visual appeal, photos, graphics, company colors (see attached Sample Colors for the appropriate shades of orange and blue), cover page with full image
Nice to have
• Sample brochures included in the upload section should be a great starting point. Placeholders for key facts, maps, team member photos, etc. would be great.
Should not have
• too much content, too much space for paragraphs and language

```html
<!DOCTYPE html>
<html lang="en">
<head>
<meta charset="utf-8">
<title>Halvern Residential Group – Capabilities Overview</title>
<link href="https://fonts.googleapis.com/css2?family=Open+Sans:wght@400;600;700&display=swap" rel="stylesheet">
<style>
  :root {
    --blue: #0655a3;
    --orange: #f78f20;
    --gray: #333333;
    --gray-mid: #777777;
    --gray-bar: #9a9a9a;
    --paper: #ffffff;
    --backdrop: #eeeeee;
    --ink: #141414;
  }
  * { box-sizing: border-box; margin: 0; padding: 0; }
  html, body { width: 1200px; height: 2400px; overflow: hidden; }
  body {
    background: var(--backdrop);
    font-family: "Open Sans", Arial, sans-serif;
    color: var(--gray);
    position: relative;
  }
  .spread { position: absolute; left: 30px; width: 1140px; height: 740px; display: flex; gap: 20px; }
  .spread--outside { top: 400px; }
  .spread--inside { top: 1240px; }
  .page {
    position: relative; width: 560px; height: 740px;
    background: var(--paper); overflow: hidden;
    box-shadow: 0 2px 10px rgba(0,0,0,0.12);
  }
  .sky-band {
    position: absolute; left: 0; top: 0; width: 100%; height: 115px;
    background:
      radial-gradient(ellipse 30% 40% at 20% 95%, rgba(255,255,255,0.95), rgba(255,255,255,0) 70%),
      radial-gradient(ellipse 35% 45% at 62% 100%, rgba(255,255,255,0.95), rgba(255,255,255,0) 70%),
      radial-gradient(ellipse 25% 35% at 90% 90%, rgba(255,255,255,0.85), rgba(255,255,255,0) 70%),
      linear-gradient(180deg, #0d4fae 0%, #2f6fc6 45%, #8db2e2 80%, #eef3fa 100%);
  }
  .footer-band { position: absolute; left: 0; bottom: 0; width: 100%; height: 66px; background: var(--blue); }
  .small { font-size: 7px; line-height: 10px; color: var(--gray-mid); }
  .small strong { color: var(--gray); font-weight: 700; }

  /* back page */
  .team { position: absolute; top: 145px; left: 50px; right: 50px; display: flex; justify-content: space-between; }
  .team-member { width: 100px; }
  .team-photo {
    width: 80px; height: 80px; border-radius: 50%;
    border: 3px solid var(--blue);
    background: radial-gradient(circle at 50% 40%, #dbe6f4 0%, #b7cbe6 100%);
    margin-left: 4px;
  }
  .team-member p { margin-top: 14px; }
  .about { position: absolute; top: 300px; left: 50px; width: 460px; }
  .about p + p { margin-top: 9px; }

  /* cover */
  .brand {
    position: absolute; top: 330px; left: 0; width: 100%;
    display: flex; align-items: center; justify-content: center; gap: 16px;
  }
  .brand-mark { width: 46px; height: 46px; background: var(--orange); flex: none; }
  .brand-name {
    color: var(--orange); font-size: 30px; font-weight: 600;
    line-height: 36px; letter-spacing: 0.5px; text-align: left;
  }

  /* inside pages */
  .top-band { position: absolute; top: 0; left: 0; width: 100%; height: 122px; display: flex; }
  .band-text {
    background: var(--blue); color: #fff; width: 310px; padding: 18px 22px;
    font-size: 7px; line-height: 10.5px; flex: none;
  }
  .photo { height: 100%; flex: 1; position: relative; }
  .photo--houses {
    background:
      linear-gradient(180deg, rgba(0,0,0,0) 72%, #5f8a3a 72%, #4d7430 100%),
      linear-gradient(90deg, rgba(0,0,0,0) 18%, #e8e2d4 18%, #e8e2d4 48%, #b9a27e 48%, #b9a27e 58%, #ece6da 58%, #ece6da 86%, rgba(0,0,0,0) 86%) 0 45% / 100% 40% no-repeat,
      linear-gradient(180deg, #6fa3dc 0%, #bcd6ef 60%);
  }
  .photo--play {
    background:
      linear-gradient(180deg, rgba(0,0,0,0) 62%, #c2844f 62%, #a56a3a 100%),
      linear-gradient(90deg, rgba(0,0,0,0) 30%, #3f6a9c 30%, #3f6a9c 40%, #d9a33a 40%, #d9a33a 52%, rgba(0,0,0,0) 52%) 0 42% / 100% 22% no-repeat,
      linear-gradient(180deg, #8db8e3 0%, #6f9a55 55%, #5c8744 62%);
  }
  .section-title {
    position: absolute; top: 148px; left: 30px;
    font-size: 9px; font-weight: 600; color: var(--gray);
  }
  .chart { position: absolute; }
  .caption { position: absolute; width: 220px; }
  .bottom-band { position: absolute; left: 0; bottom: 0; width: 100%; height: 140px; display: flex; }
  .bottom-band .band-text { width: 230px; }
  .photo--kitchen {
    flex: none; width: 160px;
    background:
      linear-gradient(180deg, rgba(0,0,0,0) 55%, #2e2620 55%, #1f1914 100%),
      linear-gradient(90deg, #d9a86a 0%, #b97c42 40%, #8a5a2e 70%, #d8c9b2 100%);
  }
  .dark-note {
    flex: 1; background: var(--ink); color: #fff; padding: 22px 18px;
    font-size: 9px; line-height: 12px; font-weight: 600;
  }
  .photo--homes {
    background:
      linear-gradient(180deg, rgba(0,0,0,0) 78%, #6c8a44 78%, #55703a 100%),
      linear-gradient(90deg, #a4876a 0%, #c9ab88 30%, #e1d3bf 30%, #e1d3bf 55%, #b28b63 55%, #8c6a4c 100%) 0 100% / 100% 65% no-repeat,
      linear-gradient(180deg, #9cc0e6 0%, #cfe0f2 100%);
  }
  .photo-label { position: absolute; top: 12px; right: 14px; font-size: 8px; color: #fff; font-weight: 600; }
  .bottom-band--right .band-text { width: 310px; }
</style>
</head>
<body>

<section class="spread spread--outside">
  <article class="page page--back">
    <div class="sky-band" role="img" aria-label="Blue sky with white clouds"></div>
    <div class="team">
      <div class="team-member">
        <div class="team-photo" role="img" aria-label="Team member portrait"></div>
        <p class="small"><strong>Name Here</strong><br>Title of role<br>Short bio line here</p>
      </div>
      <div class="team-member">
        <div class="team-photo" role="img" aria-label="Team member portrait"></div>
        <p class="small"><strong>Name Here</strong><br>Title of role<br>Short bio line here</p>
      </div>
      <div class="team-member">
        <div class="team-photo" role="img" aria-label="Team member portrait"></div>
        <p class="small"><strong>Name Here</strong><br>Title of role<br>Short bio line here</p>
      </div>
      <div class="team-member">
        <div class="team-photo" role="img" aria-label="Team member portrait"></div>
        <p class="small"><strong>Name Here</strong><br>Title of role<br>Short bio line here</p>
      </div>
    </div>
    <div class="about small">
      <p><strong>About our team.</strong> We manage multifamily communities for owners who value steady returns and well kept homes.</p>
      <p>Our local staff handles leasing, upkeep, reporting and resident care so investors can focus on growing their portfolio with confidence.</p>
      <p>Contact us today to learn how we can support your next property.</p>
    </div>
    <div class="footer-band"></div>
  </article>

  <article class="page page--cover">
    <div class="sky-band" role="img" aria-label="Blue sky with white clouds"></div>
    <div class="brand">
      <span class="brand-mark"></span>
      <h1 class="brand-name">Halvern<br>Residential Group</h1>
    </div>
    <div class="footer-band"></div>
  </article>
</section>

<section class="spread spread--inside">
  <article class="page page--inside-left">
    <div class="top-band">
      <p class="band-text">Professional management for multifamily owners, with clear reporting, strong leasing and hands-on care for every community we serve.</p>
      <div class="photo photo--houses" role="img" aria-label="Photo of apartment townhomes under blue sky"></div>
    </div>
    <h2 class="section-title">Occupancy and leasing results</h2>
    <svg class="chart" style="left:50px;top:195px" width="170" height="170" viewBox="0 0 170 170" aria-label="Pie chart">
      <circle cx="85" cy="85" r="75" fill="var(--orange)"/>
      <path d="M85 85 L85 10 A75 75 0 0 1 156 62 Z" fill="#8c8c8c"/>
    </svg>
    <svg class="chart" style="left:300px;top:185px" width="230" height="200" viewBox="0 0 230 200" aria-label="Bar chart">
      <line x1="10" y1="0" x2="10" y2="200" stroke="#d9d9d9" stroke-width="1"/>
      <rect x="10" y="10" width="200" height="16" fill="var(--orange)"/>
      <rect x="10" y="42" width="185" height="16" fill="var(--orange)"/>
      <rect x="10" y="74" width="165" height="16" fill="var(--orange)"/>
      <rect x="10" y="106" width="150" height="16" fill="var(--orange)"/>
      <rect x="10" y="138" width="130" height="16" fill="var(--orange)"/>
      <rect x="10" y="170" width="110" height="16" fill="var(--orange)"/>
      <polyline points="20,180 70,140 120,105 165,70 200,45" fill="none" stroke="var(--gray)" stroke-width="1.5"/>
    </svg>
    <p class="caption small" style="left:40px;top:400px">Average occupancy across our managed portfolio stays high year over year.</p>
    <p class="caption small" style="left:310px;top:400px">Lease renewals rise as resident service improves.</p>
    <div class="bottom-band">
      <p class="band-text">We keep owners informed with monthly statements, budgets and clear updates on every property.</p>
      <div class="photo photo--kitchen" role="img" aria-label="Photo of a modern apartment kitchen"></div>
      <p class="dark-note">Quality upgrades that raise value</p>
    </div>
  </article>

  <article class="page page--inside-right">
    <div class="top-band">
      <p class="band-text">From lease-up to long-term operations, our team brings proven systems to every community in the region.</p>
      <div class="photo photo--play" role="img" aria-label="Photo of a community playground"></div>
    </div>
    <h2 class="section-title">Services and key facts</h2>
    <svg class="chart" style="left:30px;top:185px" width="240" height="150" viewBox="0 0 240 150" aria-label="Table">
      <rect x="0" y="0" width="240" height="20" fill="var(--orange)"/>
      <g stroke="var(--orange)" stroke-width="1">
        <line x1="0" y1="45" x2="240" y2="45"/>
        <line x1="0" y1="70" x2="240" y2="70"/>
        <line x1="0" y1="95" x2="240" y2="95"/>
        <line x1="0" y1="120" x2="240" y2="120"/>
        <line x1="0" y1="145" x2="240" y2="145"/>
        <line x1="80" y1="20" x2="80" y2="145"/>
        <line x1="160" y1="20" x2="160" y2="145"/>
      </g>
    </svg>
    <svg class="chart" style="left:320px;top:185px" width="200" height="150" viewBox="0 0 200 150" aria-label="Key facts list">
      <circle cx="12" cy="12" r="10" fill="var(--orange)"/><rect x="34" y="8" width="160" height="8" fill="var(--gray-bar)"/>
      <circle cx="12" cy="44" r="10" fill="var(--orange)"/><rect x="34" y="40" width="160" height="8" fill="var(--gray-bar)"/>
      <circle cx="12" cy="76" r="10" fill="var(--orange)"/><rect x="34" y="72" width="160" height="8" fill="var(--gray-bar)"/>
      <circle cx="12" cy="108" r="10" fill="var(--orange)"/><rect x="34" y="104" width="160" height="8" fill="var(--gray-bar)"/>
      <circle cx="12" cy="140" r="10" fill="var(--orange)"/><rect x="34" y="136" width="160" height="8" fill="var(--gray-bar)"/>
    </svg>
    <p class="caption small" style="left:30px;top:360px">Leasing, maintenance, accounting and resident relations under one roof.</p>
    <p class="caption small" style="left:320px;top:360px">Local teams, fast response and transparent owner reporting.</p>
    <div class="bottom-band bottom-band--right">
      <p class="band-text">Partner with a firm that treats your property like its own and your residents like neighbors.</p>
      <div class="photo photo--homes" role="img" aria-label="Photo of apartment building exteriors">
        <span class="photo-label">Welcome home</span>
      </div>
    </div>
  </article>
</section>

</body>
</html>
```